Playful, Modern Brochure Design for informing about managed services provided

For our Managed Services we are looking for a brochure with simple explanation of the services we offer. Brochure not a full text brochure. Something like a summation with prices of the options we provide. Think about monitoring, VOIP, anti-virus, tessera 480 etc.

combination of Who We Are and products offering in a simple overview.

a bit similar to https://leaflet.pimovarta.com/contest.aspx?id=3847102

it’s about professional services, security and stability of the customers IT, so the design should express that.

Target Market(s)

Business to Business

Font styles to use
Sans Serif
Other font styles liked:
• Arial

Colors

Designer to choose colors to be used in the design.

Requirements
Must have
• attractive front which invites to read further, inside summation of services.
• Contact Info
• Icons for services:
• Hosting, Security, Monitoring, Cloud, VOIP, Online Backup
Nice to have
• Other icons like Tessera 480, firewall, proxy server and other thinkable.
Should not have
• Pages with large amount of text.

```html
<!DOCTYPE html>
<html lang="en">
<head>
<meta charset="utf-8">
<title>Vantor Service Division Flyer</title>
<link href="https://fonts.googleapis.com/css2?family=Bebas+Neue&family=Open+Sans:wght@400;600;700&display=swap" rel="stylesheet">
<style>
  :root {
    --blue: #1ba1dc;
    --brown: #4f4841;
    --white: #ffffff;
    --icon-label: #5a524b;
    --photo-light: #eef1f4;
    --photo-mid: #c9d3dc;
  }
  * { box-sizing: border-box; margin: 0; padding: 0; }
  html, body { width: 937px; height: 1200px; overflow: hidden; background: var(--white); }
  .flyer { position: relative; width: 937px; height: 1200px; font-family: "Open Sans", Arial, sans-serif; }

  .hero-photo {
    position: absolute; left: 0; top: 0; width: 937px; height: 346px;
    background: linear-gradient(100deg, var(--photo-light) 0%, var(--photo-mid) 45%, #8fa2b4 70%, var(--photo-light) 100%);
  }
  .brand { position: absolute; left: 72px; top: 66px; display: flex; align-items: center; gap: 10px; }
  .brand-dot { width: 26px; height: 26px; border-radius: 50%; background: var(--blue); }
  .brand-name { font-family: "Open Sans", Arial, sans-serif; font-weight: 600; font-size: 34px; color: var(--blue); letter-spacing: 1px; }

  .title-band {
    position: absolute; left: 0; top: 346px; width: 937px; height: 172px;
    background: var(--blue); color: var(--white); text-align: center;
  }
  .title-band h1 { font-family: "Bebas Neue", Arial, sans-serif; font-weight: 400; font-size: 68px; letter-spacing: 3px; line-height: 1; margin-top: 32px; }
  .title-band p { font-family: "Bebas Neue", Arial, sans-serif; font-size: 32px; letter-spacing: 1px; margin-top: 10px; }

  .services { position: absolute; left: 0; top: 518px; width: 937px; height: 245px; }
  .service { position: absolute; top: 52px; width: 180px; text-align: center; }
  .service svg { display: block; margin: 0 auto; }
  .service-label { font-family: "Bebas Neue", Arial, sans-serif; font-size: 29px; color: var(--icon-label); margin-top: 14px; }
  .service--monitoring { left: 112px; }
  .service--antivirus { left: 375px; }
  .service--voip { left: 620px; }

  .info { position: absolute; top: 763px; width: 468px; height: 262px; color: var(--white); text-align: center; padding: 0 20px; }
  .info--who { left: 0; background: var(--blue); }
  .info--products { left: 468px; width: 469px; background: var(--brown); }
  .info h2 { font-weight: 700; font-size: 29px; margin-top: 40px; }
  .info p { font-size: 19px; line-height: 22.5px; margin-top: 22px; }

  .cta { position: absolute; left: 0; top: 1035px; width: 937px; height: 113px; background: var(--blue); color: var(--white); text-align: center; font-weight: 700; font-size: 19px; line-height: 24px; padding-top: 32px; }
  .footer { position: absolute; left: 0; top: 1148px; width: 937px; height: 52px; background: var(--brown); color: var(--white); text-align: center; font-size: 17px; line-height: 52px; }
</style>
</head>
<body>
<div class="flyer">
  <div class="hero-photo" role="img" aria-label="Photo of four smiling business colleagues gathered around a desk in a bright office"></div>
  <div class="brand"><span class="brand-dot"></span><span class="brand-name">VANTOR</span></div>

  <section class="title-band">
    <h1>Service Division</h1>
    <p>Quick Response, Quality Results</p>
  </section>

  <section class="services">
    <div class="service service--monitoring">
      <svg width="112" height="106" viewBox="0 0 112 106" fill="#1ba1dc">
        <rect x="32" y="0" width="48" height="34" rx="3"/><rect x="52" y="34" width="8" height="6"/><rect x="44" y="40" width="24" height="4"/>
        <rect x="0" y="56" width="48" height="36" rx="3"/><rect x="20" y="92" width="8" height="6"/><rect x="12" y="98" width="24" height="4"/>
        <rect x="64" y="56" width="48" height="36" rx="3"/><rect x="84" y="92" width="8" height="6"/><rect x="76" y="98" width="24" height="4"/>
        <path d="M6 48V14h18v4H10v30z M106 48V14H88v4h14v30z"/>
      </svg>
      <div class="service-label">Monitoring</div>
    </div>
    <div class="service service--antivirus">
      <svg width="90" height="106" viewBox="0 0 90 106">
        <path d="M4 4h82v56c0 20-20 34-41 43C24 94 4 80 4 60z" fill="#1ba1dc"/>
        <path d="M14 14h62v45c0 15-15 26-31 33C29 85 14 74 14 59z" fill="#fff"/>
        <path d="M22 22h46v37c0 11-11 20-23 25C33 79 22 70 22 59z" fill="#1ba1dc"/>
        <path d="M31 52l10 10 18-20" stroke="#fff" stroke-width="7" fill="none" stroke-linecap="round" stroke-linejoin="round"/>
      </svg>
      <div class="service-label">Anti-Virus</div>
    </div>
    <div class="service service--voip">
      <svg width="90" height="100" viewBox="0 0 90 100" fill="#1ba1dc">
        <path d="M12 0h66l10 30H2z"/>
        <path d="M35 8c-3 6 2 14 10 16l3-4-5-3-2 2c-2-1-4-3-4-6l2-1-1-5z" fill="#fff"/>
        <rect x="0" y="40" width="90" height="26" rx="4"/>
        <rect x="50" y="51" width="20" height="4" fill="#fff"/>
        <rect x="41" y="66" width="8" height="20"/>
        <rect x="0" y="86" width="90" height="6"/>
        <circle cx="45" cy="89" r="8"/>
      </svg>
      <div class="service-label">VoIP</div>
    </div>
  </section>

  <section class="info info--who">
    <h2>Who We Are</h2>
    <p>Lorem ipsum dolor sit amet, consectetur adipiscing elit. In aliquam fringilla ex, ut iaculis turpis. Vivamus varius magna vitae leo tincidunt, non fermentum metus iaculis. Class aptent taciti sociosqu ad litora torquent</p>
  </section>
  <section class="info info--products">
    <h2>Our Products</h2>
    <p>Lorem ipsum dolor sit amet, consectetur adipiscing elit. In aliquam fringilla ex, ut iaculis turpis. Vivamus varius magna vitae leo tincidunt, non fermentum metus iaculis. Class aptent taciti sociosqu ad litora torquent</p>
  </section>

  <section class="cta">Are you looking for a reliable partner that will make your automation<br>always in top condition? Vantor take this task like themselves.</section>
  <footer class="footer">Lindenhof 7, 5711 KP Helmond, Phone: 088-0149320, www.vantor.nl</footer>
</div>
</body>
</html>
```